Makeup Artist Requires Business Card design

Hi

I am looking for a business card design to market my makeup artist business. I operate under my own name Mara Veldt and I would like to keep the design of the card very simplistic and chic - something that keeps both my name and profession (makeup artist) the focus of the card. I would like it to be a style that is eyecatching to the reader (i am open to anything unusual) but upmarket.

Target Market(s)

women, magazine/beauty/fashion editors, photographers.

Industry/Entity Type

Business

Requirements
Must have
• Must contain:

Phone number: 0418 372 915
Website: www.maraveldt.com.au
email: contact@maraveldt.com.au

(although you don't need to have prefaced these with the words phone number, website etc :))
Should not have
• I am not looking for anything overly colorful - my preference is to keep the card dark if possible.

```html
<!DOCTYPE html>
<html lang="en">
<head>
<meta charset="utf-8">
<title>Mara Veldt – Makeup Artist Business Card</title>
<link rel="stylesheet" href="https://fonts.googleapis.com/css2?family=Playball&family=Marcellus&display=swap">
<style>
  :root {
    --page-bg: #d9d7d5;
    --card-dark: #3b2d2f;
    --band-cream: #eeebe1;
    --ink-dark: #3b2d2f;
    --ink-light: #f1eee6;
    --ornament-tone: #b9b2a8;
  }
  html, body {
    margin: 0;
    padding: 0;
    width: 1200px;
    height: 900px;
    overflow: hidden;
    background: var(--page-bg);
  }
  .business-card {
    position: absolute;
    left: 170px;
    top: 204px;
    width: 860px;
    height: 492px;
    background: var(--card-dark);
    box-shadow: 0 10px 30px rgba(0, 0, 0, 0.25);
    overflow: hidden;
  }
  .name-band {
    position: absolute;
    left: 0;
    top: 132px;
    width: 100%;
    height: 150px;
    background: var(--band-cream);
  }
  .identity {
    position: absolute;
    left: 0;
    top: 18px;
    width: 100%;
    text-align: center;
    color: var(--ink-dark);
  }
  .identity-name {
    margin: 0;
    font-family: "Playball", cursive;
    font-weight: 400;
    font-size: 66px;
    line-height: 1.1;
  }
  .identity-role {
    margin: -4px 0 0;
    font-family: "Marcellus", serif;
    font-size: 18px;
    letter-spacing: 2px;
  }
  .flourish {
    position: absolute;
    border-radius: 6px;
  }
  .flourish-left { left: 180px; top: 84px; }
  .flourish-right { left: 592px; top: 16px; }
  .contact-details {
    position: absolute;
    left: 0;
    top: 310px;
    width: 100%;
    margin: 0;
    text-align: center;
    font-family: "Marcellus", serif;
    font-size: 21px;
    line-height: 30px;
    color: var(--ink-light);
    list-style: none;
    padding: 0;
  }
</style>
</head>
<body>
  <article class="business-card">
    <div class="name-band">
      <svg class="flourish flourish-left" width="100" height="50" role="img" aria-label="Decorative scroll flourish">
        <rect width="100" height="50" rx="8" fill="var(--ornament-tone)" opacity="0.45"/>
      </svg>
      <svg class="flourish flourish-right" width="100" height="50" role="img" aria-label="Decorative scroll flourish">
        <rect width="100" height="50" rx="8" fill="var(--ornament-tone)" opacity="0.45"/>
      </svg>
      <div class="identity">
        <h1 class="identity-name">Mara Veldt</h1>
        <p class="identity-role">Makeup Artist</p>
      </div>
    </div>
    <ul class="contact-details">
      <li class="contact-phone">P: 0418 372 915</li>
      <li class="contact-email">contact@maraveldt.com.au</li>
      <li class="contact-web">www.maraveldt.com.au</li>
    </ul>
  </article>
</body>
</html>
```